Urgent Care Postcard Launch

We are launching a pediatric only urgent care. The postcard will be hand-delivered to local medical providers and business owners.
Updates

Reason: I was traveling with spotty internet and was unable to provide feedback. Thanks for your understanding!

All designs need to have a focus on Urgent Care. Where the lines say "opening soon" it needs to be specific to Urgent Care as a we are already open for primary care. Thanks.

Target Market(s)

Parents/grandparents of children 0-17 years old.

Industry/Entity Type

Medical

Requirements
Must have
• Opening date of September 1, 2014
Hours of operation - weekdays 5pm-9pm/weekends and holidays 9am-5pm
Phone #(405)555-0193
website - www.larchfieldmd.com
Logo
List of things we can treat (see previous flyers)

```html
<!DOCTYPE html>
<html lang="en">
<head>
<meta charset="utf-8">
<title>Pediatric Urgent Care Postcard</title>
<link href="https://fonts.googleapis.com/css2?family=Questrial&family=Montserrat:wght@500;700&display=swap" rel="stylesheet">
<style>
  :root{
    --backdrop:#5f6062;
    --card:#ffffff;
    --ink:#2b2b2b;
    --title-grey:#8a8b8d;
    --sun:#fcbf18;
    --sun-deep:#f6b30f;
    --red:#d4232b;
    --green:#3aa646;
    --line:#9a9a9a;
  }
  *{margin:0;padding:0;box-sizing:border-box;}
  html,body{width:787px;height:1200px;overflow:hidden;}
  body{background:var(--backdrop);position:relative;font-family:"Questrial",sans-serif;color:var(--ink);}

  .card{position:absolute;left:49px;width:689px;background:var(--card);overflow:hidden;}
  .card--front{top:50px;height:528px;}
  .card--back{top:622px;height:500px;}

  /* front */
  .headline{position:absolute;left:40px;top:34px;font-size:45px;line-height:45px;color:var(--title-grey);letter-spacing:.5px;font-weight:400;}
  .photo{position:absolute;left:0;top:120px;width:689px;height:275px;
    background:linear-gradient(180deg,#fbf7f3 0%,#f3dcc8 35%,#e8b99c 62%,#e46a4a 82%,#d9566e 100%);}
  .badge{position:absolute;left:494px;top:-30px;width:190px;height:190px;border-radius:50%;background:var(--sun);
    color:#fff;text-align:center;font-family:"Montserrat",sans-serif;font-weight:700;padding-top:55px;}
  .badge__main{font-size:27px;line-height:27px;display:block;}
  .badge__date{font-size:15px;line-height:20px;display:block;margin-top:5px;}

  .brand{position:absolute;display:flex;align-items:center;gap:10px;}
  .brand__mark{width:22px;height:22px;background:var(--red);}
  .brand__name{font-size:24px;color:var(--ink);}
  .card--front .brand{left:28px;top:465px;}

  .contact{position:absolute;left:270px;top:407px;width:410px;text-align:center;}
  .contact__phone{font-size:23px;color:var(--red);}
  .contact__web{font-family:"Montserrat",sans-serif;font-weight:700;font-size:19px;color:var(--green);margin-top:3px;}
  .contact__hours-title{font-size:17px;margin-top:10px;}
  .contact__hours{font-size:15px;margin-top:4px;}

  /* back */
  .intro{position:absolute;left:29px;top:30px;width:295px;font-size:14px;line-height:19px;}
  .intro strong{font-family:"Montserrat",sans-serif;font-weight:700;font-size:13px;}
  .card--back .brand{left:358px;top:50px;}
  .card--back .brand__mark{width:18px;height:18px;}
  .card--back .brand__name{font-size:18px;}
  .address{position:absolute;left:361px;top:96px;font-size:14px;line-height:20px;}
  .stamp{position:absolute;left:587px;top:44px;width:77px;height:87px;border:1px solid var(--line);}
  .addr-line{position:absolute;left:410px;width:212px;height:1px;background:var(--line);}

  .services-shadow{position:absolute;left:24px;top:168px;width:276px;height:250px;background:var(--sun-deep);
    border-radius:14px;transform:rotate(-4deg);}
  .services{position:absolute;left:33px;top:157px;width:283px;height:246px;background:#fff;border:4px solid var(--sun);
    border-radius:14px;transform:rotate(-4deg);padding:14px 0 0 16px;}
  .services__title{font-family:"Montserrat",sans-serif;font-weight:700;font-size:14px;color:var(--green);letter-spacing:.3px;}
  .services__list{list-style:none;margin-top:6px;}
  .services__list li{display:flex;align-items:center;gap:8px;font-size:14px;height:24.5px;}
  .services__list svg{flex:none;}

  .cta{position:absolute;left:0;top:444px;width:350px;text-align:center;font-size:17.5px;line-height:23px;color:var(--green);}
  .cta .red{color:var(--red);}
</style>
</head>
<body>

<section class="card card--front">
  <h1 class="headline">PEDIATRIC<br>URGENT CARE</h1>
  <div class="photo" role="img" aria-label="Photo of four smiling children lying side by side with chins resting on their hands"></div>
  <div class="badge"><span class="badge__main">OPENING<br>SOON</span><span class="badge__date">SEPTEMBER<br>1, 2014</span></div>
  <div class="brand"><span class="brand__mark"></span><span class="brand__name">Larchfield Pediatrics</span></div>
  <div class="contact">
    <p class="contact__phone">CALL NOW : (405)555-0193</p>
    <p class="contact__web">WWW.LARCHFIELDMD.COM</p>
    <p class="contact__hours-title">HOURS OF OPERATION</p>
    <p class="contact__hours">weekdays 5pm-9pm/weekends and holidays 9am-5pm</p>
  </div>
</section>

<section class="card card--back">
  <p class="intro">When your child gets sick the illness often seems to escalate quickly. That's why at Larchfield Pediatrics we offer <strong>full service pediatric care!</strong> We are dedicated to giving your children high quality care when they need it the most.</p>
  <div class="brand"><span class="brand__mark"></span><span class="brand__name">Larchfield Pediatrics</span></div>
  <p class="address">4417 SW 86th<br>Oklahoma City, OK 73159</p>
  <div class="stamp"></div>
  <div class="addr-line" style="top:214px"></div>
  <div class="addr-line" style="top:259px"></div>
  <div class="addr-line" style="top:303px"></div>

  <div class="services-shadow"></div>
  <div class="services">
    <h2 class="services__title">OUR SERVICES INCLUDE:</h2>
    <ul class="services__list">
      <li><svg width="14" height="14" viewBox="0 0 14 14"><circle cx="7" cy="7" r="7" fill="#d4232b"/><path d="M3.8 7.2l2.2 2.2 4.2-4.4" stroke="#fff" stroke-width="1.8" fill="none"/></svg>Pediatric primary care</li>
      <li><svg width="14" height="14" viewBox="0 0 14 14"><circle cx="7" cy="7" r="7" fill="#d4232b"/><path d="M3.8 7.2l2.2 2.2 4.2-4.4" stroke="#fff" stroke-width="1.8" fill="none"/></svg>Vaccinations</li>
      <li><svg width="14" height="14" viewBox="0 0 14 14"><circle cx="7" cy="7" r="7" fill="#d4232b"/><path d="M3.8 7.2l2.2 2.2 4.2-4.4" stroke="#fff" stroke-width="1.8" fill="none"/></svg>Flu shots</li>
      <li><svg width="14" height="14" viewBox="0 0 14 14"><circle cx="7" cy="7" r="7" fill="#d4232b"/><path d="M3.8 7.2l2.2 2.2 4.2-4.4" stroke="#fff" stroke-width="1.8" fill="none"/></svg>No hospital wait time</li>
      <li><svg width="14" height="14" viewBox="0 0 14 14"><circle cx="7" cy="7" r="7" fill="#d4232b"/><path d="M3.8 7.2l2.2 2.2 4.2-4.4" stroke="#fff" stroke-width="1.8" fill="none"/></svg>Easy access location</li>
      <li><svg width="14" height="14" viewBox="0 0 14 14"><circle cx="7" cy="7" r="7" fill="#d4232b"/><path d="M3.8 7.2l2.2 2.2 4.2-4.4" stroke="#fff" stroke-width="1.8" fill="none"/></svg>Great hours</li>
      <li><svg width="14" height="14" viewBox="0 0 14 14"><circle cx="7" cy="7" r="7" fill="#d4232b"/><path d="M3.8 7.2l2.2 2.2 4.2-4.4" stroke="#fff" stroke-width="1.8" fill="none"/></svg>Electronic Medical Records</li>
      <li><svg width="14" height="14" viewBox="0 0 14 14"><circle cx="7" cy="7" r="7" fill="#d4232b"/><path d="M3.8 7.2l2.2 2.2 4.2-4.4" stroke="#fff" stroke-width="1.8" fill="none"/></svg>One on One medical attention</li>
    </ul>
  </div>

  <p class="cta">MAKE YOUR APPOINTMENT WITH<br><span class="red">LARCHFIELD PEDIATRICS</span> TODAY.</p>
</section>

</body>
</html>
```